Business Card for a Floral & Decorating Business

I would like to take my current logo and create a better business card. I am looking for elegance as I am a florist and event decorator. My logo has multiple colour options. I like colours like green, purple, pink and orange, I think I would like a white card, open to black back ground. I want it to feel elegant and romantic. I like metallic lettering that maybe is indented in the paper, I also like glossy paper. I have a full logo already as well as a badge. I have attached both in multiple colours.m
Updates

Need extra days to review

Target Market(s)

Weddings, special events, floral customers

Industry/Entity Type

Floral and decorating

Contact Information for Business Card

Phone number, email, instagram, facebook, title, name, logo

Font styles to use
Script

Requirements
Nice to have
• Elegant

```html
<!DOCTYPE html>
<html lang="en">
<head>
<meta charset="UTF-8">
<title>Elowen Marsh Business Card</title>
<link href="https://fonts.googleapis.com/css2?family=Great+Vibes&family=Pinyon+Script&family=Cormorant+Garamond:wght@500&family=Montserrat:wght@400&display=swap" rel="stylesheet">
<style>
  :root {
    --backdrop: #1b1b1c;
    --card: #1e1e1f;
    --card-sheen: #2c2b2b;
    --rose-gold: #e9b7a3;
    --ivory: #f4f0ee;
  }
  * { margin: 0; padding: 0; box-sizing: border-box; }
  html, body { width: 1200px; height: 900px; overflow: hidden; }
  body {
    background: radial-gradient(ellipse at 60% 40%, #2a2a2b 0%, var(--backdrop) 70%);
    display: flex; flex-direction: column; align-items: center; justify-content: center; gap: 36px;
  }
  .card {
    position: relative;
    width: 700px; height: 400px;
    background: linear-gradient(125deg, var(--card) 40%, var(--card-sheen) 80%, var(--card) 100%);
    box-shadow: 0 18px 40px rgba(0,0,0,0.55);
  }
  /* Front */
  .front-brand {
    position: absolute; left: 0; right: 0; top: 120px;
    text-align: center;
    font-family: "Great Vibes", cursive;
    font-size: 92px; color: var(--rose-gold); line-height: 1;
  }
  .front-tagline {
    position: absolute; left: 0; right: 0; top: 250px;
    text-align: center;
    font-family: "Cormorant Garamond", serif;
    font-weight: 500; font-size: 17px; letter-spacing: 7px;
    color: var(--rose-gold);
  }
  /* Back */
  .holder { position: absolute; left: 48px; top: 44px; }
  .holder-name {
    font-family: "Pinyon Script", cursive;
    font-size: 44px; color: var(--rose-gold); line-height: 1;
  }
  .holder-title {
    font-family: "Montserrat", sans-serif;
    font-size: 15px; color: var(--ivory); margin-top: 4px; letter-spacing: 0.5px;
  }
  .social {
    position: absolute; right: 48px; top: 90px;
    display: flex; align-items: center; gap: 12px;
  }
  .social-handle {
    font-family: "Great Vibes", cursive; font-size: 24px; color: var(--ivory);
  }
  .social-mark { width: 18px; height: 18px; border-radius: 50%; background: var(--rose-gold); }
  .back-brand {
    position: absolute; left: 44px; top: 190px;
    font-family: "Great Vibes", cursive;
    font-size: 74px; color: var(--rose-gold); line-height: 0.85;
  }
  .back-brand .line-two { display: block; padding-left: 60px; }
  .contact {
    position: absolute; right: 48px; bottom: 44px;
    font-family: "Montserrat", sans-serif; font-size: 19px; color: var(--ivory);
    text-align: right; line-height: 1.45;
  }
  .contact-row { display: flex; align-items: center; justify-content: flex-end; gap: 10px; }
  .contact-icon { width: 16px; height: 16px; }
</style>
</head>
<body>
  <section class="card card-front">
    <div class="front-brand">elowen marsh</div>
    <div class="front-tagline">DECORATING &amp; FLORALS.</div>
  </section>

  <section class="card card-back">
    <div class="holder">
      <div class="holder-name">Julian Hartley</div>
      <div class="holder-title">Director</div>
    </div>

    <div class="social">
      <span class="social-handle">elowenmarsh</span>
      <span class="social-mark"></span>
    </div>

    <div class="back-brand">elowen<span class="line-two">marsh</span></div>

    <div class="contact">
      <div class="contact-row">
        <span>(555) 318-2046</span>
        <svg class="contact-icon" viewBox="0 0 24 24" fill="none" stroke="#e9b7a3" stroke-width="2" stroke-linecap="round" stroke-linejoin="round">
          <path d="M5 3h4l2 5-2.5 1.5a11 11 0 0 0 6 6L16 13l5 2v4a2 2 0 0 1-2 2A16 16 0 0 1 3 5a2 2 0 0 1 2-2z"/>
        </svg>
      </div>
      <div class="contact-row">
        <span>elowenmarsh@mail.com</span>
        <svg class="contact-icon" viewBox="0 0 24 24" fill="none" stroke="#e9b7a3" stroke-width="2" stroke-linejoin="round">
          <rect x="3" y="5" width="18" height="14" rx="1"/>
          <path d="M3 6l9 7 9-7"/>
        </svg>
      </div>
    </div>
  </section>
</body>
</html>
```